Finance Company need Staff ID card & Patio umbrella design

We need the following design:
1. Employee ID Card (Vertical ID Card)
2. Patio Umbrella
3. Uniform (light grey collar shirt)

Please note that our company theme is grey and gold (yellow). Any mixture is fine as well as long it's simple, nice and unique.

Website: www.lnt-example.com.kh

Reason: Dear all We would like to extend deadline for 5 days more.

Target Market(s)

Public

Industry/Entity Type

Bank

Requirements
Must have
• 1. ID Card, information needed:
• - Name of the company: LNT Microfinance Ltd
• - Staff name
• - Position
• - ID #
• - Expiry Date
• - Photo
• - Message at the back of ID: This card is property of LNT Mirofinance Ltd. If found, Please return to LNT Microfinance Ltd 023 417 395.
• 2- Patio Umbrella only need company name
• 3- Uniform only need company and color design.
Nice to have
• Gold (or Yellow) and/or grey (Light)

```html
<!DOCTYPE html>
<html lang="en">
<head>
<meta charset="utf-8">
<title>LNT Microfinance – Staff ID Card</title>
<link href="https://fonts.googleapis.com/css2?family=Tenor+Sans&display=swap" rel="stylesheet">
<style>
  :root {
    --canvas: #ffffff;
    --card: #333235;
    --gold: #d3a32a;
    --gold-light: #e6bb3f;
    --gold-deep: #a97d17;
    --medal: #e9b81f;
    --medal-text: #5e420c;
    --cream: #f4ecd0;
    --ink-light: #ffffff;
    --photo-a: #7e9a63;
    --photo-b: #c9ccd3;
  }
  * { margin: 0; padding: 0; box-sizing: border-box; }
  html, body { width: 1200px; height: 1200px; overflow: hidden; background: var(--canvas); }
  body { position: relative; font-family: "Tenor Sans", sans-serif; color: var(--ink-light); }

  .card { position: absolute; top: 151px; width: 540px; height: 899px; background: var(--card); overflow: hidden; }
  .card--back { left: 23px; }
  .card--front { left: 601px; }
  .card svg { position: absolute; left: 0; top: 0; }

  .return-note {
    position: absolute; left: 0; right: 0; top: 688px;
    text-align: center; font-size: 21px; line-height: 25.5px; letter-spacing: 0.2px;
  }

  .stripe-band {
    position: absolute; left: 155px; width: 229px;
    background: repeating-linear-gradient(90deg, var(--gold) 0 2px, var(--gold-light) 2px 3px);
  }
  .stripe-band--top { top: 0; height: 569px; }
  .stripe-band--bottom { top: 739px; height: 160px; }

  .photo-frame {
    position: absolute; left: 75px; top: 50px; width: 392px; height: 389px;
    border: 9px solid var(--medal); background: var(--medal);
  }
  .photo-frame .photo {
    width: 100%; height: 100%;
    background: linear-gradient(180deg, var(--photo-a) 0%, #6f8a58 45%, var(--photo-b) 100%);
  }

  .staff-details {
    position: absolute; left: 30px; top: 590px;
    display: grid; grid-template-columns: 184px auto; row-gap: 0;
    font-size: 19px; line-height: 23.8px; letter-spacing: 0.3px;
  }
</style>
</head>
<body>

<section class="card card--back">
  <svg width="540" height="899" viewBox="0 0 540 899" aria-hidden="true">
    <defs>
      <pattern id="pinstripe" width="3" height="10" patternUnits="userSpaceOnUse">
        <rect width="3" height="10" fill="#d3a32a"/>
        <rect x="2" width="1" height="10" fill="#e6bb3f"/>
      </pattern>
    </defs>
    <polygon class="ribbon-tail" points="60,286 155,286 155,336 60,336 82,311" fill="#d3a32a" stroke="#555" stroke-width="2"/>
    <polygon class="ribbon-tail" points="384,286 477,286 455,311 477,336 384,336" fill="#d3a32a" stroke="#555" stroke-width="2"/>
    <polygon class="ribbon-band" points="155,0 384,0 384,551 269,479 155,551" fill="url(#pinstripe)"/>
    <circle class="medal" cx="264" cy="265" r="145" fill="#e9b81f"/>
    <text x="264" y="258" text-anchor="middle" font-family="Tenor Sans, sans-serif" font-size="30" fill="#5e420c">LNT</text>
    <text x="264" y="292" text-anchor="middle" font-family="Tenor Sans, sans-serif" font-size="22" fill="#5e420c">MICROFINANCE</text>
    <line x1="75" y1="670" x2="465" y2="670" stroke="#f4ecd0" stroke-width="2.5"/>
    <line x1="75" y1="808" x2="465" y2="808" stroke="#f4ecd0" stroke-width="2.5"/>
  </svg>
  <p class="return-note">
    This card is property of LNT Mirofinance Ltd.<br>
    If found, Please return to<br>
    LNT Microfinance Ltd<br>
    023 417 395
  </p>
</section>

<section class="card card--front">
  <div class="stripe-band stripe-band--top"></div>
  <div class="stripe-band stripe-band--bottom"></div>
  <div class="photo-frame">
    <div class="photo" role="img" aria-label="Staff portrait photo"></div>
  </div>
  <dl class="staff-details">
    <dt>Compnay Name:</dt><dd>LNT Microfinance Ltd.</dd>
    <dt>Name :</dt><dd>Rashed Karim Talukder</dd>
    <dt>Possition :</dt><dd>Assistant Manager</dd>
    <dt>ID:</dt><dd>#990011</dd>
    <dt>Expiry Date :</dt><dd>23/4/2019</dd>
  </dl>
</section>

</body>
</html>
```